business card for a shoe shop

we would like a business card for a family owned shoe shop.
With this information included.
Darnell's Shoe Store
Family owned since 1947

then on other side
Darnell's Shoe Store
Footwear fitting specialist
Phone: 9187 2630
218 Quarry St, Fernleigh Downs 3187
(cnr. Hartwick Rd and Quarry St)
darnellshoes218@examplemail.com
if could incorporate the purple color on card i have attached.

```html
<!DOCTYPE html>
<html lang="en">
<head>
<meta charset="utf-8">
<title>Darnell's Shoe Store – Business Card</title>
<link href="https://fonts.googleapis.com/css2?family=Crimson+Text:wght@400;600&display=swap" rel="stylesheet">
<style>
  :root {
    --purple: #8430ff;
    --white: #ffffff;
    --mist-light: #f4f6fa;
    --mist-dark: #d3d8e2;
    --ink: #1c1c1c;
    --shoe-light: #f2f2f2;
    --shoe-mid: #c9cbc6;
  }
  * { margin: 0; padding: 0; box-sizing: border-box; }
  html, body { width: 1200px; height: 1200px; overflow: hidden; background: var(--white); }
  body { position: relative; font-family: "Crimson Text", Georgia, serif; }

  .card {
    position: absolute;
    left: 139px;
    width: 930px;
    height: 531px;
    overflow: hidden;
    background: linear-gradient(160deg, var(--mist-dark) 0%, var(--mist-light) 55%, #e3e7ee 100%);
  }
  .card--front { top: 55px; }
  .card--back  { top: 621px; background: linear-gradient(200deg, var(--mist-light) 0%, #f8f9fb 45%, #e4e7ed 100%); }

  .card__shapes { position: absolute; inset: 0; width: 930px; height: 531px; }

  .shoe-artwork {
    position: absolute;
    border-radius: 40% 30% 20% 20%;
    background: radial-gradient(ellipse at 45% 55%, var(--shoe-light) 0%, var(--shoe-mid) 100%);
    opacity: 0.95;
  }
  .card--front .shoe-artwork { left: 347px; top: 37px; width: 242px; height: 202px; }
  .card--back  .shoe-artwork { left: 52px; top: 123px; width: 293px; height: 247px; }

  .front__name {
    position: absolute;
    left: 0; right: 0; top: 270px;
    text-align: center;
    color: var(--white);
    font-size: 70px;
    font-weight: 400;
    line-height: 78px;
    letter-spacing: 1px;
    text-transform: uppercase;
  }
  .front__tagline {
    position: absolute;
    left: 0; right: 0; top: 459px;
    text-align: center;
    color: var(--purple);
    font-size: 38px;
    line-height: 44px;
  }

  .back__details {
    position: absolute;
    left: 450px; width: 460px; top: 102px;
    text-align: center;
    color: var(--ink);
  }
  .back__name {
    color: var(--purple);
    font-size: 39px;
    line-height: 44px;
    font-weight: 600;
    text-transform: uppercase;
    white-space: nowrap;
  }
  .back__role {
    font-size: 23px;
    line-height: 30px;
    font-weight: 600;
    text-transform: uppercase;
    letter-spacing: 0.5px;
    margin-bottom: 48px;
  }
  .back__line { font-size: 25px; line-height: 35px; }
  .back__phone-number { color: var(--purple); }
  .back__email {
    margin-top: 52px;
    color: var(--purple);
    font-size: 20px;
    line-height: 26px;
  }
</style>
</head>
<body>

  <section class="card card--front">
    <svg class="card__shapes" viewBox="0 0 930 531" aria-hidden="true">
      <path d="M0,0 H930 V304 Q700,439 465,439 Q230,439 0,304 Z" fill="var(--purple)"/>
      <path d="M0,245 Q120,330 258,393 Q110,350 0,282 Z" fill="var(--white)"/>
      <path d="M930,245 Q810,330 672,393 Q820,350 930,282 Z" fill="var(--white)"/>
    </svg>
    <div class="shoe-artwork" role="img" aria-label="Illustration of a white peep-toe high heel shoe"></div>
    <h1 class="front__name">Darnell's Shoe<br>Store</h1>
    <p class="front__tagline">Family owned since 1947</p>
  </section>

  <section class="card card--back">
    <svg class="card__shapes" viewBox="0 0 930 531" aria-hidden="true">
      <path d="M371,0 C440,110 480,340 414,531 L374,531 C420,380 430,170 371,0 Z" fill="var(--purple)"/>
      <path d="M0,0 H371 C380,14 388,28 395,42 C440,170 420,380 299,531 H0 Z" fill="var(--purple)"/>
      <path d="M371,0 C430,100 455,260 412,330 C430,230 410,100 371,0 Z" fill="var(--white)"/>
    </svg>
    <div class="shoe-artwork" role="img" aria-label="Illustration of a white peep-toe high heel shoe"></div>
    <div class="back__details">
      <h2 class="back__name">Darnell's Shoe Store</h2>
      <p class="back__role">Footwear Fitting Specialist</p>
      <p class="back__line">Phone: <span class="back__phone-number">9187 2630</span></p>
      <p class="back__line">218 Quarry St, Fernleigh Downs 3187</p>
      <p class="back__line">(cnr. Hartwick Rd and Quarry St)</p>
      <p class="back__email">darnellshoes218@examplemail.com</p>
    </div>
  </section>

</body>
</html>
```